Business Card Design

I need a business card for my tutoring service. Key elements on front are its contact details and visual appeal with these three points: All aspects of literacy and numeracy, 'Bright Pathways Support' provider and Prep-readiness sessions
Updates

contact me by email on korawen7@mailtrove.net as I'm having issues with other address at times. Thanks

:) 

Target Market(s)

People with children

Industry/Entity Type

Tutoring

Contact Information for Business Card

Tessa Brindle Educational Consultant
17 Quillon Grove
Tarrowin 4821
0487 316 912

Requirements
Nice to have
• Something related to education. On the back of the card, my business name and phone number again, along with: spelling, reading, writing, comprehension, oral language, listening skills

```html
<!DOCTYPE html>
<html lang="en">
<head>
<meta charset="utf-8">
<title>Tessa Brindle – Educational Consultant Business Card</title>
<link rel="stylesheet" href="https://fonts.googleapis.com/css2?family=Montserrat:wght@300;400&display=swap">
<style>
  :root {
    --page-bg: #e9e7e3;
    --card-blue-light: #4d6fd6;
    --card-blue: #2f4fb4;
    --card-blue-deep: #17277a;
    --ink-white: #ffffff;
    --board-frame: #9c907a;
    --board-dark: #3f3f42;
    --board-mid: #56565a;
    --motif-tint: rgba(255, 255, 255, 0.16);
  }
  html, body {
    margin: 0;
    padding: 0;
    width: 1200px;
    height: 900px;
    overflow: hidden;
    background: var(--page-bg);
    font-family: "Montserrat", sans-serif;
  }
  .canvas {
    position: relative;
    width: 1200px;
    height: 900px;
  }
  .card {
    position: absolute;
    left: 250px;
    width: 700px;
    height: 400px;
    border-radius: 4px;
    overflow: hidden;
    color: var(--ink-white);
    background: linear-gradient(160deg, var(--card-blue-light) 0%, var(--card-blue) 45%, var(--card-blue-deep) 100%);
    box-shadow: 0 10px 24px rgba(0, 0, 0, 0.25);
    text-transform: uppercase;
    font-weight: 300;
    text-align: center;
  }
  .card--front { top: 40px; }
  .card--back { top: 470px; }

  /* Front */
  .front-heading {
    position: absolute;
    top: 78px;
    left: 0;
    right: 0;
    margin: 0;
    font-weight: 300;
    font-size: 27px;
    line-height: 1.2;
    letter-spacing: 1px;
  }
  .services-list {
    position: absolute;
    top: 182px;
    left: 0;
    right: 0;
    margin: 0;
    padding: 0;
    list-style: none;
    font-size: 17px;
    line-height: 1.25;
    letter-spacing: 0.5px;
  }
  .address {
    position: absolute;
    top: 292px;
    left: 0;
    right: 0;
    margin: 0;
    font-size: 15px;
    letter-spacing: 1px;
    font-style: normal;
  }
  .rule-pair {
    position: absolute;
  }
  .rule-pair--left { left: 40px; top: 322px; }
  .rule-pair--right { right: 40px; top: 84px; }
  .rule-pair--bottom { left: 120px; top: 350px; }
  .motif {
    position: absolute;
    background: var(--motif-tint);
    border-radius: 3px;
  }
  .motif--book { width: 62px; height: 22px; }
  .motif--pencil { width: 10px; height: 34px; }

  /* Back */
  .board {
    position: absolute;
    top: 30px;
    left: 170px;
    width: 360px;
    height: 200px;
    box-sizing: border-box;
    border: 8px solid var(--board-frame);
    background: linear-gradient(135deg, var(--board-mid), var(--board-dark));
    display: flex;
    align-items: center;
    justify-content: center;
  }
  .skills-list {
    margin: 0;
    padding: 0;
    list-style: none;
    font-size: 19px;
    line-height: 1.18;
    letter-spacing: 1px;
  }
  .board-ledge {
    position: absolute;
    bottom: 4px;
    left: 150px;
    width: 44px;
    height: 4px;
    background: #8a8a8a;
  }
  .back-heading {
    position: absolute;
    top: 250px;
    left: 0;
    right: 0;
    margin: 0;
    font-weight: 300;
    font-size: 20px;
    line-height: 1.2;
    letter-spacing: 1px;
  }
  .phone {
    position: absolute;
    top: 312px;
    left: 0;
    right: 0;
    margin: 0;
    font-size: 19px;
    letter-spacing: 1px;
    display: flex;
    align-items: center;
    justify-content: center;
    gap: 8px;
  }
</style>
</head>
<body>
<main class="canvas">

  <section class="card card--front" aria-label="Business card front">
    <span class="motif motif--book" style="left:250px;top:30px" role="img" aria-label="Open book line drawing"></span>
    <span class="motif motif--pencil" style="left:620px;top:30px" role="img" aria-label="Pencil line drawing"></span>
    <span class="motif motif--pencil" style="left:70px;top:120px" role="img" aria-label="Pencil line drawing"></span>
    <span class="motif motif--book" style="left:40px;top:250px" role="img" aria-label="Open book line drawing"></span>
    <span class="motif motif--book" style="left:600px;top:200px" role="img" aria-label="Stacked books line drawing"></span>
    <span class="motif motif--pencil" style="left:200px;top:330px" role="img" aria-label="Pencil line drawing"></span>
    <span class="motif motif--pencil" style="left:560px;top:340px" role="img" aria-label="Pencil line drawing"></span>

    <svg class="rule-pair rule-pair--right" width="90" height="10" aria-hidden="true">
      <line x1="0" y1="2" x2="90" y2="2" stroke="#fff" stroke-width="1.5"/>
      <line x1="0" y1="7" x2="90" y2="7" stroke="#fff" stroke-width="1.5"/>
    </svg>
    <svg class="rule-pair rule-pair--bottom" width="460" height="10" aria-hidden="true">
      <line x1="0" y1="2" x2="460" y2="2" stroke="#fff" stroke-width="1.5"/>
      <line x1="0" y1="7" x2="460" y2="7" stroke="#fff" stroke-width="1.5"/>
    </svg>

    <h1 class="front-heading">Tessa Brindle<br>Educational Consultant</h1>
    <ul class="services-list">
      <li>All aspects of literacy and numeracy</li>
      <li>'Bright Pathways Support' provider</li>
      <li>Prep-readiness sessions</li>
    </ul>
    <address class="address">17 Quillon Grove Tarrowin 4821</address>
  </section>

  <section class="card card--back" aria-label="Business card back">
    <div class="board">
      <ul class="skills-list">
        <li>Spelling</li>
        <li>Reading</li>
        <li>Writing</li>
        <li>Comprehension</li>
        <li>Oral language</li>
        <li>Listening skills</li>
      </ul>
      <span class="board-ledge" aria-hidden="true"></span>
    </div>
    <h2 class="back-heading">Tessa Brindle<br>Educational Consultant</h2>
    <p class="phone">
      <svg width="18" height="18" viewBox="0 0 18 18" aria-hidden="true">
        <circle cx="9" cy="9" r="9" fill="#fff"/>
        <path d="M5.5 7.5c1 2.5 2.5 4 5 5l1.3-1.3 2 1-.6 1.6c-4.5.2-8.8-4-8.6-8.6l1.6-.6 1 2z" fill="#2f4fb4"/>
      </svg>
      <span>0487 316 912</span>
    </p>
  </section>

</main>
</body>
</html>
```